Borrowdale Equity Business Card

Looking for a design for our business cards. Need to look corporate and outstanding. I have enclosed our logos for the company. Borrowdale equity is an investment firm for high level clients looking for advisory in their investments. White background or black is good. We will like to double sided options maybe at the back with just the logo of the firm.

Example of the info for the business card:

Marcus Heller
Managing Director

Panama Phone +507 391 4786
Switzerland Phone +41 43 917 2648
test@borrowdale-equity-example.com
www.borrowdale-equity-example.com

Industry/Entity Type

Investment

```html
<!DOCTYPE html>
<html lang="en">
<head>
<meta charset="utf-8">
<title>Borrowdale Equity Business Card</title>
<link rel="stylesheet" href="https://fonts.googleapis.com/css2?family=Federo&family=Sorts+Mill+Goudy&display=swap">
<style>
  :root {
    --ink: #000000;
    --paper: #ffffff;
    --gold: #a97c1b;
    --navy: #12357a;
    --navy-faint: #060b16;
  }
  * { margin: 0; padding: 0; box-sizing: border-box; }
  html, body {
    width: 835px;
    height: 1200px;
    overflow: hidden;
    background: var(--paper);
  }
  .sheet {
    position: relative;
    width: 835px;
    height: 1200px;
  }
  .card {
    position: absolute;
    left: 0;
    width: 835px;
    background: var(--ink);
  }
  .card--front { top: 0; height: 541px; }
  .card--back { top: 660px; height: 540px; }

  .holder-name {
    position: absolute;
    left: 52px;
    top: 34px;
    font-family: "Federo", sans-serif;
    font-size: 31px;
    color: var(--gold);
    letter-spacing: 0.5px;
  }
  .holder-title {
    position: absolute;
    left: 45px;
    top: 74px;
    font-family: "Sorts Mill Goudy", serif;
    font-size: 22px;
    color: var(--gold);
  }
  .front-rule {
    position: absolute;
    left: 290px;
    top: 57px;
    width: 545px;
    height: 14px;
    background: var(--gold);
  }
  .front-wordmark {
    position: absolute;
    left: 40px;
    top: 190px;
    width: 740px;
    text-align: center;
    font-family: "Federo", sans-serif;
    font-size: 72px;
    letter-spacing: 3px;
    color: var(--navy-faint);
    white-space: nowrap;
  }
  .contact {
    position: absolute;
    right: 30px;
    top: 378px;
    text-align: right;
    font-family: "Federo", sans-serif;
    color: var(--gold);
    font-variant: small-caps;
    letter-spacing: 1px;
  }
  .contact p { font-size: 21px; line-height: 28px; }
  .contact p.contact__web { font-size: 17px; font-variant: normal; text-transform: uppercase; line-height: 27px; }

  .back-band {
    position: absolute;
    left: 0;
    width: 835px;
    height: 11px;
    background: var(--gold);
  }
  .back-band--top { top: 0; }
  .back-band--bottom { bottom: 0; }
  .back-mark {
    position: absolute;
    left: 0;
    top: 240px;
    width: 835px;
    display: flex;
    align-items: center;
    justify-content: center;
    gap: 18px;
  }
  .back-mark__square {
    width: 34px;
    height: 34px;
    background: var(--gold);
  }
  .back-mark__name {
    font-family: "Federo", sans-serif;
    font-size: 52px;
    letter-spacing: 2px;
    color: var(--navy);
  }
</style>
</head>
<body>
<main class="sheet">
  <section class="card card--front">
    <h1 class="holder-name">Marcus Heller</h1>
    <p class="holder-title">Managing Director</p>
    <div class="front-rule"></div>
    <p class="front-wordmark">Borrowdale Equity</p>
    <address class="contact">
      <p>Panama Phone +507 391 4786</p>
      <p>Switzerland Phone +41 43 917 2648</p>
      <p class="contact__web">test@borrowdale-equity-example.com</p>
      <p class="contact__web">www.borrowdale-equity-example.com</p>
    </address>
  </section>

  <section class="card card--back">
    <div class="back-band back-band--top"></div>
    <div class="back-mark">
      <span class="back-mark__square"></span>
      <span class="back-mark__name">Borrowdale Equity</span>
    </div>
    <div class="back-band back-band--bottom"></div>
  </section>
</main>
</body>
</html>
```